Business Card Design for digital storytelling business

I need a business card for a workshop/consulting/coaching business.

Company Name: Bright Harbor Works

Tagline: New Ways to Keep Old Family Tales

What we do: Through workshops, webinars, and coaching we teach you how to capture, tell and share your important memories and stories using readily available digital tools. We will help you tell your life story in a format to share with your family now and in the future.
Updates

I just received a toll free number that I would like included on the designs. If the addition of a phone number would significantly alter your design, please submit an altered version. The number is 866-217-9086

Target Market(s)

Adults in US between ages of 35-70 interested in capturing, preserving and sharing memories and life stories in a digital format.
Could include the following:

-People touched by illness or tragedy who need to tell their own or a loved one's life story
-Grandparents wanting to share stories and wisdom with grandchildren living far away
-People with aging parents who want to capture their stories in a format to pass on to their children
-Alzheimer's patients and their families
-People wanting to transfer analog photos to digital; or wanting to organize digital photos into something that tells a story

Industry/Entity Type

Digital

Requirements
Must have
• Must include business name, logo, tagline

Contact information (see file)
Social media information

Fonts easily readable by aging eyes. Good contrast.

Nice to have
• Color preferences: blue, green, yellow/gold
Blue denotes the calm, non-pressured way that I teach. It is for the healing that comes from telling your story. It represents time and space that are bridged in the digital environment.
Green is for growth, the future, the family tree, Vines that grow and branch and connect the generations and our hearts.
Yellow/gold is for the legacy of wisdom in our lives and stories. It is for the light of truth we bring to the world by sharing our stories.
Should not have
• No old-style, script fonts.
No Times New Roman

```html
<!DOCTYPE html>
<html lang="en">
<head>
<meta charset="utf-8">
<title>Bright Harbor Works – Business Card</title>
<link rel="stylesheet" href="https://fonts.googleapis.com/css2?family=Open+Sans:wght@400;600;700&display=swap">
<style>
  :root {
    --backdrop: #e9e7e4;
    --card-white: #fbfbfb;
    --navy: #213e69;
    --navy-deep: #1b345b;
    --navy-light: #2b4a74;
    --ink-on-navy: #f2f5f9;
    --muted-on-navy: #c9d3e0;
    --icon-chip: #4a4f58;
    --green: #2f9a4c;
  }
  * { box-sizing: border-box; margin: 0; padding: 0; }
  html, body { width: 1200px; height: 914px; overflow: hidden; }
  body {
    background: var(--backdrop);
    font-family: "Open Sans", Arial, sans-serif;
    display: flex;
    flex-direction: column;
    align-items: center;
    justify-content: center;
    gap: 60px;
  }
  .card {
    width: 620px;
    height: 354px;
    border-radius: 4px;
    box-shadow: 0 6px 18px rgba(0,0,0,.18);
    position: relative;
    overflow: hidden;
  }
  /* Front */
  .card--front {
    background: var(--card-white);
    display: flex;
    align-items: center;
    justify-content: center;
  }
  .brand { display: flex; align-items: center; gap: 14px; }
  .brand__mark {
    width: 16px; height: 16px; border-radius: 50%;
    background: var(--green);
    flex: none;
  }
  .brand__text { display: flex; flex-direction: column; }
  .brand__name {
    font-size: 34px; font-weight: 600; color: var(--navy);
    line-height: 1.1;
    white-space: nowrap;
  }
  .brand__tagline {
    margin-top: 4px;
    font-size: 10.5px; letter-spacing: .08em; text-transform: uppercase;
    color: var(--navy);
    white-space: nowrap;
  }
  /* Back */
  .card--back {
    background: radial-gradient(ellipse at 45% 40%, var(--navy-light), var(--navy-deep) 80%);
    color: var(--ink-on-navy);
  }
  .card--back .brand {
    position: absolute; left: 40px; top: 112px; gap: 10px;
  }
  .card--back .brand__mark { width: 11px; height: 11px; background: var(--ink-on-navy); }
  .card--back .brand__name { font-size: 21px; color: var(--ink-on-navy); }
  .card--back .brand__tagline { font-size: 7px; color: var(--ink-on-navy); margin-top: 2px; }
  .divider {
    position: absolute; left: 308px; top: 48px; width: 1px; height: 258px;
    background: rgba(255,255,255,.45);
  }
  .person { position: absolute; left: 336px; top: 66px; }
  .person__name { font-size: 21px; font-weight: 700; letter-spacing: .01em; }
  .person__role { font-size: 14px; color: var(--muted-on-navy); margin-top: 2px; }
  .contacts {
    position: absolute; left: 336px; top: 142px; right: 20px;
    list-style: none; display: flex; flex-direction: column; gap: 5px;
  }
  .contacts li { display: flex; align-items: center; gap: 10px; font-size: 13px; white-space: nowrap; }
  .contacts svg { width: 14px; height: 14px; flex: none; }
</style>
</head>
<body>

  <section class="card card--front" aria-label="Card front">
    <div class="brand">
      <span class="brand__mark" aria-hidden="true"></span>
      <div class="brand__text">
        <span class="brand__name">Bright Harbor Works</span>
        <span class="brand__tagline">New Ways to Keep Old Family Tales</span>
      </div>
    </div>
  </section>

  <section class="card card--back" aria-label="Card back">
    <div class="brand">
      <span class="brand__mark" aria-hidden="true"></span>
      <div class="brand__text">
        <span class="brand__name">Bright Harbor Works</span>
        <span class="brand__tagline">New Ways to Keep Old Family Tales</span>
      </div>
    </div>

    <div class="divider" aria-hidden="true"></div>

    <div class="person">
      <div class="person__name">Maren Holloway</div>
      <div class="person__role">Founder</div>
    </div>

    <ul class="contacts">
      <li>
        <svg viewBox="0 0 14 14" aria-hidden="true"><circle cx="7" cy="7" r="7" fill="#4a4f58"/><circle cx="7" cy="7" r="3.6" fill="none" stroke="#fff" stroke-width="1"/><line x1="3.4" y1="7" x2="10.6" y2="7" stroke="#fff" stroke-width=".8"/></svg>
        www.brightharborworks.com
      </li>
      <li>
        <svg viewBox="0 0 14 14" aria-hidden="true"><circle cx="7" cy="7" r="7" fill="#4a4f58"/><rect x="3.5" y="4.6" width="7" height="4.8" fill="none" stroke="#fff" stroke-width=".9"/><polyline points="3.5,4.6 7,7.4 10.5,4.6" fill="none" stroke="#fff" stroke-width=".9"/></svg>
        maren@brightharborworks.com
      </li>
      <li>
        <svg viewBox="0 0 14 14" aria-hidden="true"><circle cx="7" cy="7" r="7" fill="#4a4f58"/><polygon points="7,3.4 10.6,6.6 9.6,6.6 9.6,10 4.4,10 4.4,6.6 3.4,6.6" fill="#fff"/></svg>
        PO Box 218, Elm Crossing, RI 02960
      </li>
      <li>
        <svg viewBox="0 0 14 14" aria-hidden="true"><circle cx="7" cy="7" r="7" fill="#4a4f58"/><circle cx="7" cy="7" r="2" fill="#fff"/></svg>
        www.brightharborworks.com/circle
      </li>
      <li>
        <svg viewBox="0 0 14 14" aria-hidden="true"><circle cx="7" cy="7" r="7" fill="#4a4f58"/><circle cx="7" cy="7" r="2" fill="#fff"/></svg>
        www.brightharborworks.com/boards/
      </li>
      <li>
        <svg viewBox="0 0 14 14" aria-hidden="true"><circle cx="7" cy="7" r="7" fill="#4a4f58"/><circle cx="7" cy="7" r="2" fill="#fff"/></svg>
        @BrightHarbor
      </li>
    </ul>
  </section>

</body>
</html>
```